Criação de Papelaria Profissional para Consultoria de Negócios
A empresa queria:
" Serviços de Consultoria de Carreira (transição, desenvolvimento de liderança), Assessment, Coaching, Outplacement, Headhunting "

```html
<!DOCTYPE html>
<html lang="pt-BR">
<head>
<meta charset="utf-8">
<title>Helena Moretti — Envelopes</title>
<link rel="stylesheet" href="https://fonts.googleapis.com/css2?family=Cinzel:wght@400&family=Lato:wght@400;700&display=swap">
<style>
  :root {
    --bg: #ece9e4;
    --wine-light: #8e1c26;
    --wine: #5e0f1a;
    --wine-dark: #3f0a12;
    --paper: #ffffff;
    --silver-light: #f2f2f2;
    --silver: #c9c9c9;
    --silver-dark: #a9a9a9;
    --ghost: #ecebeb;
    --ink: #3a3a3a;
  }
  * { margin: 0; padding: 0; box-sizing: border-box; }
  html, body { width: 1200px; height: 1200px; overflow: hidden; background: var(--bg); }
  .sheet { position: relative; width: 1200px; height: 1200px; }

  .envelope { position: absolute; top: 96px; width: 432px; height: 996px; }
  .envelope--front { left: 144px; }
  .envelope--back { left: 624px; }

  .envelope__flap {
    position: absolute; left: 12px; right: 12px; top: 0; height: 70px;
    border-radius: 18px 18px 0 0;
    background: linear-gradient(180deg, var(--silver-light), var(--silver) 70%, var(--silver-dark));
  }
  .envelope__body {
    position: absolute; left: 0; right: 0; top: 48px; bottom: 0;
    box-shadow: 0 6px 18px rgba(0,0,0,.18);
  }
  .envelope--front .envelope__body {
    background: radial-gradient(ellipse 70% 45% at 50% 40%, var(--wine-light), var(--wine) 55%, var(--wine-dark));
  }
  .envelope--back .envelope__body { background: var(--paper); }

  .envelope__tab {
    position: absolute; left: 72px; right: 72px; bottom: 52px; height: 26px;
    border-radius: 12px 12px 0 0;
    background: linear-gradient(180deg, var(--silver-light), var(--silver) 60%, var(--silver-dark));
  }

  .brand { position: absolute; left: 0; right: 0; top: 300px; text-align: center; color: #fff; }
  .brand__mark {
    width: 22px; height: 22px; border-radius: 50%; border: 1.5px solid #fff;
    margin: 0 auto 36px;
  }
  .brand__name {
    font-family: "Cinzel", serif; font-weight: 400; font-size: 40px; letter-spacing: 2px; line-height: 1;
  }
  .brand__tagline {
    margin-top: 12px; font-family: "Cinzel", serif; font-size: 13px; letter-spacing: 4.5px;
  }

  .ghost-name {
    position: absolute; left: 0; right: 0; top: 250px; text-align: center;
    font-family: "Cinzel", serif; font-size: 72px; line-height: 1.1; color: var(--ghost);
  }

  .footer { position: absolute; left: 22px; right: 22px; top: 750px; }
  .footer__brand {
    text-align: center; font-family: "Cinzel", serif; font-size: 13px; letter-spacing: 1px;
    color: var(--wine); margin-bottom: 14px;
  }
  .contacts { display: flex; justify-content: space-between; font-family: "Lato", sans-serif; font-size: 7.5px; line-height: 1.6; color: var(--ink); }
  .contacts__item { display: flex; align-items: center; gap: 4px; }
  .contacts__item svg { width: 9px; height: 9px; fill: var(--wine); flex: none; }
  .contacts strong { font-weight: 700; }
</style>
</head>
<body>
<main class="sheet">

  <section class="envelope envelope--front" aria-label="Envelope, frente">
    <div class="envelope__flap"></div>
    <div class="envelope__body">
      <div class="brand">
        <div class="brand__mark"></div>
        <div class="brand__name">HELENA MORETTI</div>
        <div class="brand__tagline">CONSULTORIA DE CARREIRA</div>
      </div>
      <div class="envelope__tab"></div>
    </div>
  </section>

  <section class="envelope envelope--back" aria-label="Envelope, verso">
    <div class="envelope__flap"></div>
    <div class="envelope__body">
      <div class="ghost-name" aria-hidden="true">HELENA<br>MORETTI</div>
      <div class="footer">
        <div class="footer__brand">HELENA MORETTI</div>
        <div class="contacts">
          <div>
            <div class="contacts__item"><svg viewBox="0 0 10 10"><path d="M2 1l2 2-1 1.2c.6 1.2 1.6 2.2 2.8 2.8L7 6l2 2-1.3 1.3C4.6 9 1 5.4.7 2.3z"/></svg>11 3000-0000</div>
            <div class="contacts__item"><svg viewBox="0 0 10 10"><path d="M2 1l2 2-1 1.2c.6 1.2 1.6 2.2 2.8 2.8L7 6l2 2-1.3 1.3C4.6 9 1 5.4.7 2.3z"/></svg>11 90000-0000</div>
          </div>
          <div>
            <div class="contacts__item"><svg viewBox="0 0 10 10"><circle cx="5" cy="5" r="4.5"/></svg>helenamoretti.com.br</div>
            <div class="contacts__item"><svg viewBox="0 0 10 10"><rect x="0.5" y="2" width="9" height="6" rx="1"/></svg>contato@helenamoretti.com.br</div>
          </div>
          <div>
            <div class="contacts__item"><svg viewBox="0 0 10 10"><path d="M5 0a3.5 3.5 0 0 0-3.5 3.5C1.5 6 5 10 5 10s3.5-4 3.5-6.5A3.5 3.5 0 0 0 5 0z"/></svg><span>Rua das Acácias, 120 - Centro<br><strong>São Paulo</strong> - SP - CEP 01000-000</span></div>
          </div>
        </div>
      </div>
      <div class="envelope__tab"></div>
    </div>
  </section>

</main>
</body>
</html>
```